Brinmoor Logistics - Cards and Logo

We need a logo and card design for a Logistics company located in Chicago. Our competitors are KRV and Torvan. We would like to see designs that incorporate a logo that shows all ways in terms of direction. The colors would be Electric Blue, Grays, Blacks and White. I like how Pumo has a badge type logo that is strong and clean. Quorvel also has a strong font that is futuristic. The final design should communicate we are a strong and technological type of company. I show a picture of the colors we like from a pumo cooler.

```html
<!DOCTYPE html>
<html lang="en">
<head>
<meta charset="utf-8">
<title>Brinmoor Logistics – Business Cards</title>
<link rel="stylesheet" href="https://fonts.googleapis.com/css2?family=Montserrat:wght@700;800&family=Arimo:wght@400&display=swap">
<style>
  :root {
    --backdrop: #2a2a2b;
    --card: #fbfbfb;
    --card-edge: #e6e6e6;
    --brand-gray: #6d6e70;
    --text-gray: #5b5c5e;
    --electric-blue: #2f93d8;
    --rule: #b9babc;
  }
  * { margin: 0; padding: 0; box-sizing: border-box; }
  html, body {
    width: 1200px; height: 900px; overflow: hidden;
    background: var(--backdrop);
  }
  .canvas {
    position: relative; width: 1200px; height: 900px;
    display: flex; flex-direction: column; align-items: center; justify-content: center; gap: 48px;
  }
  .card {
    position: relative; width: 640px; height: 366px;
    background: linear-gradient(160deg, #ffffff 0%, var(--card) 55%, var(--card-edge) 100%);
    border-radius: 30px;
  }
  /* logo lockup: plain square with the company name */
  .logo { display: flex; flex-direction: column; align-items: center; }
  .logo-square {
    width: 92px; height: 92px; border-radius: 10px; background: var(--brand-gray);
  }
  .logo-name {
    margin-top: 14px;
    font-family: "Montserrat", sans-serif; font-weight: 800;
    font-size: 18px; letter-spacing: 0.4px; color: var(--brand-gray);
    text-transform: uppercase; white-space: nowrap;
  }
  /* front */
  .card-front .logo { position: absolute; left: 40px; width: 260px; top: 118px; }
  .card-front .divider {
    position: absolute; left: 322px; top: 70px; width: 1px; height: 226px; background: var(--rule);
  }
  .contact { position: absolute; left: 348px; top: 86px; font-family: "Arimo", Arial, sans-serif; color: var(--text-gray); }
  .contact-name {
    font-family: "Montserrat", sans-serif; font-weight: 700; font-size: 17px;
    letter-spacing: 0.4px; color: var(--text-gray); text-transform: uppercase;
  }
  .contact-role {
    font-family: "Montserrat", sans-serif; font-weight: 700; font-size: 12.5px;
    color: var(--electric-blue); text-transform: uppercase; margin-top: 2px;
  }
  .contact-address { font-size: 14px; line-height: 18px; margin-top: 6px; }
  .contact-list { list-style: none; margin-top: 10px; }
  .contact-list li { display: flex; align-items: center; gap: 9px; font-size: 14px; height: 21px; }
  .contact-list svg { width: 15px; height: 15px; flex: none; }
  /* back */
  .card-back .logo { position: absolute; left: 0; right: 0; top: 76px; }
  .card-back .logo-square { width: 110px; height: 110px; border-radius: 12px; }
  .card-back .logo-name { font-size: 22px; }
  .card-back .website {
    position: absolute; left: 0; right: 0; top: 286px; text-align: center;
    font-family: "Arimo", Arial, sans-serif; font-size: 17px; color: var(--text-gray);
  }
</style>
</head>
<body>
<main class="canvas">

  <section class="card card-front">
    <div class="logo">
      <div class="logo-square"></div>
      <div class="logo-name">Brinmoor Logistics</div>
    </div>
    <div class="divider"></div>
    <div class="contact">
      <div class="contact-name">Dorian Ashcombe</div>
      <div class="contact-role">CEO/Founder</div>
      <div class="contact-address">742 W. Harlow Avenue<br>Suite B, Marlen, CA 93114</div>
      <ul class="contact-list">
        <li>
          <svg viewBox="0 0 16 16"><rect width="16" height="16" rx="3" fill="#2f93d8"/><path d="M5 3.5l2 2-1 1.2c.6 1.3 1.6 2.3 2.9 2.9l1.2-1 2 2-1.3 1.6C7.6 12 4 8.4 3.8 4.8z" fill="#fff"/></svg>
          555.014.2278
        </li>
        <li>
          <svg viewBox="0 0 16 16"><rect width="16" height="16" rx="3" fill="#2f93d8"/><rect x="5" y="3" width="6" height="3" fill="#fff"/><rect x="3" y="6.5" width="10" height="4.5" rx="1" fill="#fff"/><rect x="5" y="10" width="6" height="3" fill="#fff" stroke="#2f93d8" stroke-width="0.8"/></svg>
          555.014.6190
        </li>
        <li>
          <svg viewBox="0 0 16 16"><rect width="16" height="16" rx="3" fill="#2f93d8"/><rect x="3" y="4.5" width="10" height="7" fill="#fff"/><path d="M3 4.5l5 4 5-4" fill="none" stroke="#2f93d8" stroke-width="1"/></svg>
          dorian@brinmoorlogistics.com
        </li>
        <li>
          <svg viewBox="0 0 16 16"><rect width="16" height="16" rx="3" fill="#2f93d8"/><g fill="none" stroke="#fff" stroke-width="1"><circle cx="8" cy="8" r="4.5"/><ellipse cx="8" cy="8" rx="2" ry="4.5"/><path d="M3.5 8h9"/></g></svg>
          www.brinmoorlogistics.com
        </li>
      </ul>
    </div>
  </section>

  <section class="card card-back">
    <div class="logo">
      <div class="logo-square"></div>
      <div class="logo-name">Brinmoor Logistics</div>
    </div>
    <div class="website">www.brinmoorlogistics.com</div>
  </section>

</main>
</body>
</html>
```